Website for IT consulting Company

I need a website upgrade, the existing site content is ok, I would also like to add a testimonial page, the site should be something that is easy for us to update content. You use the content from www.velmarketa.com as an example. I will also post update logo and artwork. I also need a contact form with some type of validation or captcha.

Please omit Address maps

Target Market(s)

small business, service oriented companies. We provide IT Consulting, support and mangement

Industry/Entity Type

Information Technology

Coding

Coded - Design and coding required

Number of Pages Required

1 page

Font styles to use
Serif
Sans Serif

Requirements
Must have
• Contain logo attached, and content from existing web site www.velmarketa.com.
• Also need to update content easily, and be movable to different platforms.
• There is a catch phrase
• "Let us worry about your technology…” “ so you don’t have to!”
• Should be included.
Nice to have
• Testimonial page, Project page where we can post new and past projects and pictures
Should not have
• none

```html
<!DOCTYPE html>
<html lang="en">
<head>
<meta charset="utf-8">
<title>Testimonials – Velmarketa</title>
<link rel="stylesheet" href="https://fonts.googleapis.com/css2?family=Roboto:wght@400;500&family=Lato:wght@400&display=swap">
<style>
:root{
  --accent:#f2912f;
  --blue:#2a8fd4;
  --ink:#1d1d1f;
  --text:#444;
  --muted:#a8a8a8;
  --hero:#f0f1f3;
  --line:#e6e6e6;
  --footer:#23262e;
  --footer-side:#1f2228;
  --footer-text:#b9bcc2;
}
*{box-sizing:border-box;margin:0;padding:0}
html,body{width:1026px;height:1200px;overflow:hidden}
body{position:relative;background:#fff;font-family:"Roboto",sans-serif;color:var(--ink)}
a{color:inherit;text-decoration:none}

.site-header{position:absolute;left:0;top:0;width:1026px;height:48px;background:#fff}
.brand{position:absolute;left:76px;top:13px;display:flex;align-items:center;gap:6px;font-size:19px;font-weight:500;color:var(--blue);letter-spacing:.5px}
.brand-mark{width:16px;height:16px;background:var(--blue);border-radius:3px}
.main-nav{position:absolute;top:0;right:76px;display:flex;height:48px}
.main-nav a{position:relative;display:block;padding:0 11.5px;line-height:52px;font-size:11px;color:#222}
.main-nav a.active{color:var(--accent)}
.main-nav a.active::before{content:"";position:absolute;left:0;right:0;top:0;height:2px;background:var(--accent)}

.page-hero{position:absolute;left:0;top:48px;width:1026px;height:162px;background:var(--hero);text-align:center}
.page-title{margin-top:64px;font-size:26px;font-weight:500;letter-spacing:.5px;color:#1a1a1a}
.breadcrumb{margin-top:4px;font-size:11px;color:#666}
.scroll-down{position:absolute;left:499px;top:195px;width:29px;height:29px;border-radius:50%;background:#fff;box-shadow:0 2px 6px rgba(0,0,0,.15);display:flex;align-items:center;justify-content:center}

.testimonials{position:absolute;left:74px;top:282px;width:876px;display:grid;grid-template-columns:431px 431px;column-gap:14px;row-gap:15px}
.testimonial{position:relative;height:173px;border:1px solid var(--line);background:#fff}
.avatar{position:absolute;left:46px;top:40px;width:66px;height:66px;border-radius:50%;border:4px solid #f3f3f3}
.avatar.a1{background:linear-gradient(160deg,#e9eef2,#9aa6b0)}
.avatar.a2{background:linear-gradient(160deg,#c9b9a8,#6f7a86)}
.avatar.a3{background:linear-gradient(160deg,#8da0b6,#3c4652)}
.avatar.a4{background:linear-gradient(160deg,#9da4ab,#4e5154)}
.avatar.a5{background:linear-gradient(160deg,#8a6d55,#2c3140)}
.avatar.a6{background:linear-gradient(160deg,#d7e6ee,#6aa6c4)}
.quote-body{position:absolute;left:139px;top:46px;width:265px;font-family:"Lato",sans-serif}
.quote{font-size:12px;line-height:17.6px;color:var(--text)}
.stars{display:flex;gap:2.4px;margin-top:2px}
.author{margin-top:4px;font-size:12px;color:#222}
.author time{color:var(--muted)}

.site-footer{position:absolute;left:0;top:901px;width:1026px;height:299px;background:var(--footer)}
.footer-side{position:absolute;left:0;top:0;width:366px;height:299px;background:var(--footer-side);text-align:center}
.footer-brand{margin-top:102px;display:inline-flex;align-items:center;gap:8px;font-size:26px;font-weight:500;color:#fff;letter-spacing:1px}
.footer-brand .brand-mark{width:22px;height:22px;background:#fff}
.copyright{margin-top:14px;font-size:11px;line-height:17px;color:var(--footer-text)}
.footer-col{position:absolute;top:80px}
.footer-col h3{font-size:13px;font-weight:400;color:#fff}
.footer-col h3::after{content:"";display:block;width:16px;height:1px;background:#fff;margin-top:8px}
.link-list{list-style:none;margin-top:13px}
.link-list li{display:flex;align-items:center;gap:10px;height:21.3px;font-size:11px;color:var(--footer-text)}
.link-grid{display:flex;gap:48px}
.to-top{position:absolute;left:974px;top:1137px;width:32px;height:32px;border-radius:50%;background:var(--accent);display:flex;align-items:center;justify-content:center}
</style>
</head>
<body>

<header class="site-header">
  <a class="brand" href="#"><span class="brand-mark"></span>VELMARKETA</a>
  <nav class="main-nav">
    <a href="#">HOME</a><a href="#">SUPPORT</a><a href="#">PROJECTS</a><a href="#">CLIENTS</a><a class="active" href="#">TESTIMONIALS</a><a href="#">CAREERS</a><a href="#">CONTACT</a>
  </nav>
</header>

<section class="page-hero">
  <h1 class="page-title">TESTIMONIALS</h1>
  <p class="breadcrumb">Home / testimonials</p>
</section>
<a class="scroll-down" href="#">
  <svg width="9" height="6" viewBox="0 0 9 6"><path d="M1 1l3.5 3.5L8 1" fill="none" stroke="#222" stroke-width="1.5"/></svg>
</a>

<main class="testimonials">
  <article class="testimonial">
    <div class="avatar a1" role="img" aria-label="Client portrait"></div>
    <div class="quote-body">
      <p class="quote">“He was very thorough and explained everything in detail. He did an excellent job. Thank Velmarketa for the great service!”</p>
      <div class="stars"><svg width="11" height="11" viewBox="0 0 24 24"><path fill="#f2912f" d="M12 1l3.3 7.1 7.7.8-5.8 5.2 1.7 7.6L12 17.8 5.1 21.7l1.7-7.6L1 8.9l7.7-.8z"/></svg><svg width="11" height="11" viewBox="0 0 24 24"><path fill="#f2912f" d="M12 1l3.3 7.1 7.7.8-5.8 5.2 1.7 7.6L12 17.8 5.1 21.7l1.7-7.6L1 8.9l7.7-.8z"/></svg><svg width="11" height="11" viewBox="0 0 24 24"><path fill="#f2912f" d="M12 1l3.3 7.1 7.7.8-5.8 5.2 1.7 7.6L12 17.8 5.1 21.7l1.7-7.6L1 8.9l7.7-.8z"/></svg><svg width="11" height="11" viewBox="0 0 24 24"><path fill="#f2912f" d="M12 1l3.3 7.1 7.7.8-5.8 5.2 1.7 7.6L12 17.8 5.1 21.7l1.7-7.6L1 8.9l7.7-.8z"/></svg><svg width="11" height="11" viewBox="0 0 24 24"><path fill="#f2912f" d="M12 1l3.3 7.1 7.7.8-5.8 5.2 1.7 7.6L12 17.8 5.1 21.7l1.7-7.6L1 8.9l7.7-.8z"/></svg></div>
      <p class="author">John Smith - <time>July 12, 2017</time></p>
    </div>
  </article>
  <article class="testimonial">
    <div class="avatar a2" role="img" aria-label="Client portrait"></div>
    <div class="quote-body">
      <p class="quote">“He was very thorough and explained everything in detail. He did an excellent job. Thank Velmarketa for the great service!”</p>
      <div class="stars"><svg width="11" height="11" viewBox="0 0 24 24"><path fill="#f2912f" d="M12 1l3.3 7.1 7.7.8-5.8 5.2 1.7 7.6L12 17.8 5.1 21.7l1.7-7.6L1 8.9l7.7-.8z"/></svg><svg width="11" height="11" viewBox="0 0 24 24"><path fill="#f2912f" d="M12 1l3.3 7.1 7.7.8-5.8 5.2 1.7 7.6L12 17.8 5.1 21.7l1.7-7.6L1 8.9l7.7-.8z"/></svg><svg width="11" height="11" viewBox="0 0 24 24"><path fill="#f2912f" d="M12 1l3.3 7.1 7.7.8-5.8 5.2 1.7 7.6L12 17.8 5.1 21.7l1.7-7.6L1 8.9l7.7-.8z"/></svg><svg width="11" height="11" viewBox="0 0 24 24"><path fill="#f2912f" d="M12 1l3.3 7.1 7.7.8-5.8 5.2 1.7 7.6L12 17.8 5.1 21.7l1.7-7.6L1 8.9l7.7-.8z"/></svg><svg width="11" height="11" viewBox="0 0 24 24"><path fill="#f2912f" d="M12 1l3.3 7.1 7.7.8-5.8 5.2 1.7 7.6L12 17.8 5.1 21.7l1.7-7.6L1 8.9l7.7-.8z"/></svg></div>
      <p class="author">John Smith - <time>July 12, 2017</time></p>
    </div>
  </article>
  <article class="testimonial">
    <div class="avatar a3" role="img" aria-label="Client portrait"></div>
    <div class="quote-body">
      <p class="quote">“He was very thorough and explained everything in detail. He did an excellent job. Thank Velmarketa for the great service!”</p>
      <div class="stars"><svg width="11" height="11" viewBox="0 0 24 24"><path fill="#f2912f" d="M12 1l3.3 7.1 7.7.8-5.8 5.2 1.7 7.6L12 17.8 5.1 21.7l1.7-7.6L1 8.9l7.7-.8z"/></svg><svg width="11" height="11" viewBox="0 0 24 24"><path fill="#f2912f" d="M12 1l3.3 7.1 7.7.8-5.8 5.2 1.7 7.6L12 17.8 5.1 21.7l1.7-7.6L1 8.9l7.7-.8z"/></svg><svg width="11" height="11" viewBox="0 0 24 24"><path fill="#f2912f" d="M12 1l3.3 7.1 7.7.8-5.8 5.2 1.7 7.6L12 17.8 5.1 21.7l1.7-7.6L1 8.9l7.7-.8z"/></svg><svg width="11" height="11" viewBox="0 0 24 24"><path fill="#f2912f" d="M12 1l3.3 7.1 7.7.8-5.8 5.2 1.7 7.6L12 17.8 5.1 21.7l1.7-7.6L1 8.9l7.7-.8z"/></svg><svg width="11" height="11" viewBox="0 0 24 24"><path fill="#f2912f" d="M12 1l3.3 7.1 7.7.8-5.8 5.2 1.7 7.6L12 17.8 5.1 21.7l1.7-7.6L1 8.9l7.7-.8z"/></svg></div>
      <p class="author">John Smith - <time>July 12, 2017</time></p>
    </div>
  </article>
  <article class="testimonial">
    <div class="avatar a4" role="img" aria-label="Client portrait"></div>
    <div class="quote-body">
      <p class="quote">“He was very thorough and explained everything in detail. He did an excellent job. Thank Velmarketa for the great service!”</p>
      <div class="stars"><svg width="11" height="11" viewBox="0 0 24 24"><path fill="#f2912f" d="M12 1l3.3 7.1 7.7.8-5.8 5.2 1.7 7.6L12 17.8 5.1 21.7l1.7-7.6L1 8.9l7.7-.8z"/></svg><svg width="11" height="11" viewBox="0 0 24 24"><path fill="#f2912f" d="M12 1l3.3 7.1 7.7.8-5.8 5.2 1.7 7.6L12 17.8 5.1 21.7l1.7-7.6L1 8.9l7.7-.8z"/></svg><svg width="11" height="11" viewBox="0 0 24 24"><path fill="#f2912f" d="M12 1l3.3 7.1 7.7.8-5.8 5.2 1.7 7.6L12 17.8 5.1 21.7l1.7-7.6L1 8.9l7.7-.8z"/></svg><svg width="11" height="11" viewBox="0 0 24 24"><path fill="#f2912f" d="M12 1l3.3 7.1 7.7.8-5.8 5.2 1.7 7.6L12 17.8 5.1 21.7l1.7-7.6L1 8.9l7.7-.8z"/></svg><svg width="11" height="11" viewBox="0 0 24 24"><path fill="#f2912f" d="M12 1l3.3 7.1 7.7.8-5.8 5.2 1.7 7.6L12 17.8 5.1 21.7l1.7-7.6L1 8.9l7.7-.8z"/></svg></div>
      <p class="author">John Smith - <time>July 12, 2017</time></p>
    </div>
  </article>
  <article class="testimonial">
    <div class="avatar a5" role="img" aria-label="Client portrait"></div>
    <div class="quote-body">
      <p class="quote">“He was very thorough and explained everything in detail. He did an excellent job. Thank Velmarketa for the great service!”</p>
      <div class="stars"><svg width="11" height="11" viewBox="0 0 24 24"><path fill="#f2912f" d="M12 1l3.3 7.1 7.7.8-5.8 5.2 1.7 7.6L12 17.8 5.1 21.7l1.7-7.6L1 8.9l7.7-.8z"/></svg><svg width="11" height="11" viewBox="0 0 24 24"><path fill="#f2912f" d="M12 1l3.3 7.1 7.7.8-5.8 5.2 1.7 7.6L12 17.8 5.1 21.7l1.7-7.6L1 8.9l7.7-.8z"/></svg><svg width="11" height="11" viewBox="0 0 24 24"><path fill="#f2912f" d="M12 1l3.3 7.1 7.7.8-5.8 5.2 1.7 7.6L12 17.8 5.1 21.7l1.7-7.6L1 8.9l7.7-.8z"/></svg><svg width="11" height="11" viewBox="0 0 24 24"><path fill="#f2912f" d="M12 1l3.3 7.1 7.7.8-5.8 5.2 1.7 7.6L12 17.8 5.1 21.7l1.7-7.6L1 8.9l7.7-.8z"/></svg><svg width="11" height="11" viewBox="0 0 24 24"><path fill="#f2912f" d="M12 1l3.3 7.1 7.7.8-5.8 5.2 1.7 7.6L12 17.8 5.1 21.7l1.7-7.6L1 8.9l7.7-.8z"/></svg></div>
      <p class="author">John Smith - <time>July 12, 2017</time></p>
    </div>
  </article>
  <article class="testimonial">
    <div class="avatar a6" role="img" aria-label="Client portrait"></div>
    <div class="quote-body">
      <p class="quote">“He was very thorough and explained everything in detail. He did an excellent job. Thank Velmarketa for the great service!”</p>
      <div class="stars"><svg width="11" height="11" viewBox="0 0 24 24"><path fill="#f2912f" d="M12 1l3.3 7.1 7.7.8-5.8 5.2 1.7 7.6L12 17.8 5.1 21.7l1.7-7.6L1 8.9l7.7-.8z"/></svg><svg width="11" height="11" viewBox="0 0 24 24"><path fill="#f2912f" d="M12 1l3.3 7.1 7.7.8-5.8 5.2 1.7 7.6L12 17.8 5.1 21.7l1.7-7.6L1 8.9l7.7-.8z"/></svg><svg width="11" height="11" viewBox="0 0 24 24"><path fill="#f2912f" d="M12 1l3.3 7.1 7.7.8-5.8 5.2 1.7 7.6L12 17.8 5.1 21.7l1.7-7.6L1 8.9l7.7-.8z"/></svg><svg width="11" height="11" viewBox="0 0 24 24"><path fill="#f2912f" d="M12 1l3.3 7.1 7.7.8-5.8 5.2 1.7 7.6L12 17.8 5.1 21.7l1.7-7.6L1 8.9l7.7-.8z"/></svg><svg width="11" height="11" viewBox="0 0 24 24"><path fill="#f2912f" d="M12 1l3.3 7.1 7.7.8-5.8 5.2 1.7 7.6L12 17.8 5.1 21.7l1.7-7.6L1 8.9l7.7-.8z"/></svg></div>
      <p class="author">John Smith - <time>July 12, 2017</time></p>
    </div>
  </article>
</main>

<footer class="site-footer">
  <div class="footer-side">
    <div class="footer-brand"><span class="brand-mark"></span>VELMARKETA</div>
    <p class="copyright">Copyright © 2017 - Velmarketa Group, Inc -<br>All rights reserved</p>
  </div>

  <div class="footer-col" style="left:432px">
    <h3>IT SUPPORT SOLUTIONS</h3>
    <div class="link-grid">
      <ul class="link-list">
        <li><svg width="12" height="8" viewBox="0 0 12 8"><path d="M0 4h11M8 1l3 3-3 3" fill="none" stroke="#7d8088"/></svg>Network Administration</li>
        <li><svg width="12" height="8" viewBox="0 0 12 8"><path d="M0 4h11M8 1l3 3-3 3" fill="none" stroke="#7d8088"/></svg>Desktop support</li>
        <li><svg width="12" height="8" viewBox="0 0 12 8"><path d="M0 4h11M8 1l3 3-3 3" fill="none" stroke="#7d8088"/></svg>Telecommunications</li>
        <li><svg width="12" height="8" viewBox="0 0 12 8"><path d="M0 4h11M8 1l3 3-3 3" fill="none" stroke="#7d8088"/></svg>Disaster recovery</li>
        <li><svg width="12" height="8" viewBox="0 0 12 8"><path d="M0 4h11M8 1l3 3-3 3" fill="none" stroke="#7d8088"/></svg>Audio/video Multimedia</li>
        <li><svg width="12" height="8" viewBox="0 0 12 8"><path d="M0 4h11M8 1l3 3-3 3" fill="none" stroke="#7d8088"/></svg>Web design</li>
      </ul>
      <ul class="link-list">
        <li><svg width="12" height="8" viewBox="0 0 12 8"><path d="M0 4h11M8 1l3 3-3 3" fill="none" stroke="#7d8088"/></svg>Network cabling</li>
        <li><svg width="12" height="8" viewBox="0 0 12 8"><path d="M0 4h11M8 1l3 3-3 3" fill="none" stroke="#7d8088"/></svg>Wireless Networks</li>
        <li><svg width="12" height="8" viewBox="0 0 12 8"><path d="M0 4h11M8 1l3 3-3 3" fill="none" stroke="#7d8088"/></svg>Antivirus solutions</li>
        <li><svg width="12" height="8" viewBox="0 0 12 8"><path d="M0 4h11M8 1l3 3-3 3" fill="none" stroke="#7d8088"/></svg>Network security</li>
      </ul>
    </div>
  </div>

  <div class="footer-col" style="left:798px">
    <h3>Useful Links</h3>
    <ul class="link-list">
      <li><svg width="12" height="8" viewBox="0 0 12 8"><path d="M0 4h11M8 1l3 3-3 3" fill="none" stroke="#7d8088"/></svg>Home</li>
      <li><svg width="12" height="8" viewBox="0 0 12 8"><path d="M0 4h11M8 1l3 3-3 3" fill="none" stroke="#7d8088"/></svg>Support</li>
      <li><svg width="12" height="8" viewBox="0 0 12 8"><path d="M0 4h11M8 1l3 3-3 3" fill="none" stroke="#7d8088"/></svg>Projects</li>
      <li><svg width="12" height="8" viewBox="0 0 12 8"><path d="M0 4h11M8 1l3 3-3 3" fill="none" stroke="#7d8088"/></svg>Clients</li>
      <li><svg width="12" height="8" viewBox="0 0 12 8"><path d="M0 4h11M8 1l3 3-3 3" fill="none" stroke="#7d8088"/></svg>Testimonials</li>
      <li><svg width="12" height="8" viewBox="0 0 12 8"><path d="M0 4h11M8 1l3 3-3 3" fill="none" stroke="#7d8088"/></svg>Careers</li>
      <li><svg width="12" height="8" viewBox="0 0 12 8"><path d="M0 4h11M8 1l3 3-3 3" fill="none" stroke="#7d8088"/></svg>Contact</li>
    </ul>
  </div>
</footer>

<a class="to-top" href="#">
  <svg width="8" height="5" viewBox="0 0 8 5"><path d="M1 4l3-3 3 3" fill="none" stroke="#fff" stroke-width="1.3"/></svg>
</a>

</body>
</html>
```